Business Card Design

Business card design.

Business card is to have logo, website address and email address.

Website is www.brightkettle.ie
Email is info@brightkettle.ie

I have ordered Business Card Printing via Print Harbor, the Double-sided colour printed option with gloss finish.

Industry/Entity Type

Business

```html
<!DOCTYPE html>
<html lang="en">
<head>
<meta charset="utf-8">
<title>Bright Kettle – Business Card</title>
<link rel="stylesheet" href="https://fonts.googleapis.com/css2?family=Montserrat:wght@300;500;800&display=swap">
<style>
  :root {
    --page-bg: #ece7e4;
    --front-centre: #ffffff;
    --front-edge: #f6adc2;
    --back-main: #ff2a64;
    --back-deep: #f0124f;
    --brand-red: #c8102e;
    --ink-white: #ffffff;
  }
  html, body {
    margin: 0;
    width: 1200px;
    height: 900px;
    overflow: hidden;
    background: var(--page-bg);
    font-family: "Montserrat", sans-serif;
  }
  .card-sheet {
    position: relative;
    width: 1200px;
    height: 900px;
  }
  .card {
    position: absolute;
    top: 307px;
    width: 440px;
    height: 286px;
    border-radius: 4px;
    box-shadow: 0 6px 18px rgba(0,0,0,0.18);
    overflow: hidden;
  }
  .card-front {
    left: 130px;
    background: radial-gradient(ellipse at 50% 45%, var(--front-centre) 0%, var(--front-centre) 18%, var(--front-edge) 100%);
    display: flex;
    align-items: center;
    justify-content: center;
  }
  .brand-name {
    font-weight: 800;
    font-size: 32px;
    letter-spacing: 0.5px;
    color: var(--brand-red);
  }
  .card-back {
    left: 630px;
    background: linear-gradient(135deg, var(--back-main) 0%, var(--back-deep) 100%);
  }
  .back-glow {
    position: absolute;
    right: -60px;
    top: -70px;
    width: 300px;
    height: 300px;
    border-radius: 50%;
    background: radial-gradient(circle, rgba(255,255,255,0.12) 0%, rgba(255,255,255,0) 70%);
  }
  .contact-lines {
    position: absolute;
    left: 104px;
    bottom: 36px;
    color: var(--ink-white);
    line-height: 1.25;
  }
  .contact-web {
    font-weight: 500;
    font-size: 20px;
    letter-spacing: 0.5px;
  }
  .contact-email {
    font-weight: 300;
    font-size: 20px;
  }
</style>
</head>
<body>
  <main class="card-sheet">
    <section class="card card-front" aria-label="Card front">
      <span class="brand-name">BRIGHTKETTLE.IE</span>
    </section>
    <section class="card card-back" aria-label="Card back">
      <div class="back-glow" role="img" aria-label="Faint soft glow decoration"></div>
      <div class="contact-lines">
        <div class="contact-web">WWW.BRIGHTKETTLE.IE</div>
        <div class="contact-email">info@brightkettle.ie</div>
      </div>
    </section>
  </main>
</body>
</html>
```